Lantern Jubilee Flyer

I need an 8.5x11 or 8.5x14 or 11x17 flyer for a benefit concert. Logo has already been designed; uploading several different versions, and you could choose which you want to use. For flyer design: something subtly musical (not a big fan of using musical symbols in the design, treble clefs, eighth notes, etc.) But something classy. I'm uploading unformatted copy, and two logos: one of the radio station that is helping to sponsor the event, and one for the organization the concert is benefitting. This is quick turnaround, so I promise to be very responsive with feedback. Thanks!

```html
<!DOCTYPE html>
<html lang="en">
<head>
<meta charset="utf-8">
<title>Lantern Jubilee Flyer</title>
<link href="https://fonts.googleapis.com/css2?family=Montserrat:wght@700;800&family=Open+Sans:wght@400;600;700&family=Arimo:wght@400&display=swap" rel="stylesheet">
<style>
  :root {
    --paper: #f1f1f3;
    --blue: #2f6aa6;
    --link-blue: #3d86c6;
    --pink: #c2609f;
    --ink: #1d1d1f;
    --grey: #5c5c60;
    --white: #ffffff;
  }
  * { margin: 0; padding: 0; box-sizing: border-box; }
  html, body { width: 976px; height: 1200px; overflow: hidden; background: var(--paper); }
  .flyer { position: relative; width: 976px; height: 1200px; background: var(--paper); }
  .hero-art { position: absolute; left: 0; top: 0; width: 976px; height: 620px; }
  .title {
    position: absolute; left: 70px; top: 80px;
    font-family: 'Montserrat', sans-serif; font-weight: 800; color: var(--white);
    line-height: 0.92; letter-spacing: 1px;
  }
  .title-small { display: block; font-size: 84px; }
  .title-big { display: block; font-size: 150px; }
  .benefit {
    position: absolute; left: 0; top: 622px; width: 976px; text-align: center;
    font-family: 'Open Sans', sans-serif; font-weight: 700; font-size: 37px;
    line-height: 48px; color: var(--blue);
  }
  .date-band {
    position: absolute; left: 98px; top: 737px; width: 760px; height: 56px;
    background: var(--pink); color: var(--white); text-align: center;
    font-family: 'Arimo', sans-serif; font-size: 26px; line-height: 56px;
  }
  .featuring {
    position: absolute; left: 0; top: 818px; width: 976px; text-align: center;
    font-family: 'Open Sans', sans-serif; font-size: 21px; color: var(--ink);
  }
  .including {
    position: absolute; left: 0; top: 854px; width: 976px; text-align: center;
    font-family: 'Arimo', sans-serif; font-size: 15px; color: var(--grey);
  }
  .lineup {
    position: absolute; left: 50px; top: 884px; width: 876px; text-align: center;
    font-family: 'Arimo', sans-serif; font-size: 15.5px; line-height: 20px; color: var(--grey);
  }
  .beneficiary {
    position: absolute; left: 60px; top: 1030px; width: 190px; text-align: center;
    display: flex; flex-direction: column; align-items: center; gap: 8px;
  }
  .beneficiary .mark { width: 34px; height: 34px; background: var(--ink); }
  .beneficiary .name {
    font-family: 'Open Sans', sans-serif; font-weight: 600; font-size: 15px;
    line-height: 18px; color: var(--ink);
  }
  .tickets { position: absolute; left: 280px; top: 1022px; width: 416px; text-align: center; }
  .admission { font-family: 'Open Sans', sans-serif; font-weight: 600; font-size: 16px; color: var(--ink); }
  .ticket-button {
    display: block; margin: 10px auto 0; width: 392px; height: 38px; background: var(--pink);
    color: var(--white); font-family: 'Arimo', sans-serif; font-size: 19px; line-height: 38px;
    text-decoration: none;
  }
  .website {
    display: block; margin-top: 10px; font-family: 'Open Sans', sans-serif; font-weight: 700;
    font-size: 20px; color: var(--link-blue); text-decoration: none;
  }
  .sponsor {
    position: absolute; left: 718px; top: 1036px; width: 200px; text-align: center;
    display: flex; flex-direction: column; align-items: center; gap: 6px;
  }
  .sponsor .mark { width: 30px; height: 30px; border-radius: 50%; background: var(--blue); }
  .sponsor .name {
    font-family: 'Open Sans', sans-serif; font-weight: 600; font-size: 15px;
    line-height: 18px; color: var(--blue);
  }
  .venue {
    position: absolute; left: 0; top: 1136px; width: 976px; text-align: center;
    font-family: 'Open Sans', sans-serif; font-size: 21px; color: var(--blue); letter-spacing: 0.3px;
  }
</style>
</head>
<body>
<main class="flyer">
  <svg class="hero-art" viewBox="0 0 976 620" role="img" aria-label="Abstract faceted artwork in orange, red, magenta and purple with a soft grid and flowing music lines, torn along a diagonal lower edge">
    <defs>
      <linearGradient id="heroGlow" x1="0" y1="0" x2="1" y2="0.35">
        <stop offset="0" stop-color="#f08a1f"/>
        <stop offset="0.3" stop-color="#e2323a"/>
        <stop offset="0.6" stop-color="#d23878"/>
        <stop offset="0.85" stop-color="#9b3f9a"/>
        <stop offset="1" stop-color="#6a3a8e"/>
      </linearGradient>
    </defs>
    <polygon points="0,0 976,0 976,440 0,615" fill="url(#heroGlow)"/>
  </svg>

  <h1 class="title">
    <span class="title-small">MIDWINTER</span>
    <span class="title-big">LANTERN</span>
    <span class="title-big">JUBILEE</span>
  </h1>

  <h2 class="benefit">A BENEFIT FOR SANDIA STREET HEALTH ALLIANCE<br>FOR NEIGHBOURS IN NEED</h2>

  <div class="date-band">Saturday, January 13, 2018 from 12pm-8pm</div>

  <p class="featuring">Featuring some of Sierra Vista’s best musicians</p>
  <p class="including">INCLUDING:</p>
  <p class="lineup">Wind and Anvils, Tom Halvers, The Oleanda Clarinet Quartet, Neil Barstow, The Cottonwood Bassoon Band, The Daybreak Brass Quintet, Edwin Carraway, The Tin Cup Trio, Bradford Ellison, Frederic Holm, Frank Tollander, Kimberly Tollander, Fred Garland, Amy Dorsey, Dana Whitcomb, Robert Lind, Música Antigua del Valle, The Mesa Chords, The High Desert Winds, Meridian Choral Artists of the Southwest, Sun Reef Calypso, Fred Marlow, Maxine Thérond, Kevin Varennes, Toby Varennes, Jacqueline Zeller-Ward</p>

  <div class="beneficiary">
    <span class="mark"></span>
    <span class="name">Sandia Street<br>Health Alliance</span>
  </div>

  <div class="tickets">
    <p class="admission">Admission $25 ($10 for students)</p>
    <a class="ticket-button" href="#">Tickets available HERE</a>
    <a class="website" href="#">www.lanternjubileemusic.org</a>
  </div>

  <div class="sponsor">
    <span class="mark"></span>
    <span class="name">Mesa 98.1 Classical Radio<br>mesaclassical.org</span>
  </div>

  <p class="venue">ST. ALDEN’S COMMUNITY CHURCH JUNIPER FALLS, SIERRA VISTA</p>
</main>
</body>
</html>
```